Tidewell Partners Inc.
Business Card & Stationary
Tidewell Partners Inc. -
Creative Brief
Professional
Derek Holloway
President & CEO
47 Quillfern Lane Ashgrove, QL, Norlund M4R 7P9
derek@tidewellpartners.example
www.tidewellpartners.example
needs to be top drawer, classy, printing costs not a key factor
Guiding Leaders Toward Steady Growth in Revenue

```html
<!DOCTYPE html>
<html lang="en">
<head>
<meta charset="utf-8">
<title>Tidewell Partners Inc. — Stationery</title>
<link href="https://fonts.googleapis.com/css2?family=Questrial&family=Lato:wght@400;700&display=swap" rel="stylesheet">
<style>
  :root {
    --blue-deep: #0b3f8f;
    --blue: #1d5fc0;
    --blue-light: #3f86e0;
    --paper: #ffffff;
    --ink: #4a4f57;
    --rule-grey: #b9bdc4;
    --canvas: #ffffff;
    --shadow: rgba(0,0,0,0.22);
  }
  * { box-sizing: border-box; margin: 0; padding: 0; }
  html, body { width: 1200px; height: 681px; overflow: hidden; background: var(--canvas); }
  .stage { position: relative; width: 1200px; height: 681px; font-family: "Lato", Arial, sans-serif; }
  .sheet { position: absolute; background: var(--paper); box-shadow: 2px 3px 6px var(--shadow); overflow: hidden; }
  .band { position: absolute; left: 0; top: 0; width: 100%; display: block; }
  .brand { position: absolute; display: flex; align-items: center; gap: 6px; color: var(--blue); font-family: "Questrial", Arial, sans-serif; white-space: nowrap; }
  .brand .mark { background: var(--blue); display: block; }
  .address { position: absolute; color: var(--ink); line-height: 1.35; }

  /* Envelope front */
  .envelope-front { left: 60px; top: 101px; width: 444px; height: 206px; }
  .envelope-front .brand { left: 12px; top: 56px; font-size: 12px; }
  .envelope-front .brand .mark { width: 12px; height: 12px; }
  .envelope-front .address { left: 30px; top: 74px; font-size: 7px; }

  /* Envelope back */
  .envelope-back { left: 60px; top: 372px; width: 444px; height: 204px; }
  .envelope-back .flap { position: absolute; inset: 0; }
  .envelope-back .brand { left: 0; right: 0; top: 62px; flex-direction: column; gap: 5px; font-size: 11px; }
  .envelope-back .brand .mark { width: 26px; height: 26px; }

  /* Letterhead */
  .letterhead { left: 619px; top: 53px; width: 305px; height: 566px; }
  .letterhead .brand { left: 12px; top: 92px; font-size: 13px; }
  .letterhead .brand .mark { width: 22px; height: 22px; }
  .letterhead .address { left: 16px; top: 124px; font-size: 6.5px; }

  /* Business card */
  .card-front { left: 965px; top: 173px; width: 165px; height: 96px; }
  .card-front .details { position: absolute; left: 0; right: 0; top: 10px; text-align: center; color: #fff; font-size: 5.5px; line-height: 1.4; }
  .card-front .details .name { font-size: 7px; font-weight: 700; }
  .card-front .details .title { margin-bottom: 4px; }

  .card-back { left: 965px; top: 305px; width: 165px; height: 93px;
    background: radial-gradient(ellipse at center, var(--blue-light) 0%, var(--blue) 45%, var(--blue-deep) 100%); }
  .card-back .tagline { position: absolute; left: 0; right: 0; top: 42px; text-align: center; color: #fff; font-size: 5.5px; }
</style>
</head>
<body>
<main class="stage">

  <section class="sheet envelope-front" aria-label="Envelope front">
    <svg class="band" viewBox="0 0 444 46" height="46" preserveAspectRatio="none" aria-hidden="true">
      <defs>
        <linearGradient id="bandEnv" x1="0" y1="0" x2="1" y2="0">
          <stop offset="0" stop-color="#0b3f8f"/><stop offset="0.6" stop-color="#2a6fd0"/><stop offset="1" stop-color="#1d5fc0"/>
        </linearGradient>
      </defs>
      <path d="M0 0H444V18Q230 26 0 40Z" fill="url(#bandEnv)"/>
      <path d="M0 40Q230 26 444 18" fill="none" stroke="#fff" stroke-width="3"/>
      <path d="M0 44Q230 30 444 22" fill="none" stroke="#b9bdc4" stroke-width="2"/>
    </svg>
    <div class="brand"><span class="mark"></span>Tidewell Partners Inc.</div>
    <p class="address">47 Quillfern Lane<br>Ashgrove, QL, Norlund M4R 7P9</p>
  </section>

  <section class="sheet envelope-back" aria-label="Envelope back">
    <svg class="flap" viewBox="0 0 444 204" preserveAspectRatio="none" aria-hidden="true">
      <path d="M2 6L200 76Q222 84 244 76L442 6" fill="none" stroke="#c6c9ce" stroke-width="1"/>
    </svg>
    <div class="brand"><span class="mark"></span>Tidewell Partners Inc.</div>
  </section>

  <section class="sheet letterhead" aria-label="Letterhead">
    <svg class="band" viewBox="0 0 305 62" height="62" preserveAspectRatio="none" aria-hidden="true">
      <defs>
        <linearGradient id="bandLetter" x1="0" y1="0" x2="1" y2="0">
          <stop offset="0" stop-color="#0b3f8f"/><stop offset="0.6" stop-color="#2a6fd0"/><stop offset="1" stop-color="#1d5fc0"/>
        </linearGradient>
      </defs>
      <path d="M0 0H305V26Q150 34 0 54Z" fill="url(#bandLetter)"/>
      <path d="M0 54Q150 34 305 26" fill="none" stroke="#fff" stroke-width="3"/>
      <path d="M0 59Q150 39 305 31" fill="none" stroke="#b9bdc4" stroke-width="2"/>
    </svg>
    <div class="brand"><span class="mark"></span>Tidewell Partners Inc.</div>
    <p class="address">47 Quillfern Lane<br>Ashgrove, QL, Norlund M4R 7P9<br>Phone: 555-010-2040<br>www.tidewellpartners.example</p>
  </section>

  <section class="sheet card-front" aria-label="Business card front">
    <svg class="band" viewBox="0 0 165 80" height="80" preserveAspectRatio="none" aria-hidden="true">
      <defs>
        <linearGradient id="bandCard" x1="0" y1="0" x2="1" y2="0">
          <stop offset="0" stop-color="#0b3f8f"/><stop offset="0.6" stop-color="#2a6fd0"/><stop offset="1" stop-color="#1d5fc0"/>
        </linearGradient>
      </defs>
      <path d="M0 0H165V58Q80 64 0 76Z" fill="url(#bandCard)"/>
      <path d="M0 76Q80 64 165 58" fill="none" stroke="#fff" stroke-width="2"/>
      <path d="M0 80Q80 68 165 62" fill="none" stroke="#b9bdc4" stroke-width="1.5"/>
    </svg>
    <div class="details">
      <p class="name">Derek Holloway</p>
      <p class="title">President &amp; CEO</p>
      <p>47 Quillfern Lane Ashgrove, QL, Norlund M4R 7P9</p>
      <p>derek@tidewellpartners.example</p>
      <p>www.tidewellpartners.example</p>
    </div>
  </section>

  <section class="sheet card-back" aria-label="Business card back">
    <p class="tagline">Guiding Leaders Toward Steady Growth in Revenue</p>
  </section>

</main>
</body>
</html>
```